Real Estate Flyer

Hi - I am assisting a relative to sell a unit. I am looking to have a two page flyer designed (configured as a single page with back to back printing). I have uploaded two samples to give you an idea of the look and feel - one which relates to this property when originally purchased, the other for a different property.
The flyer should includes several key photos on the front along with the wording. The rear should include any secondary photos along with the floor plan.
The flyer should be close to A4 size.

Updates
Hi,
Industry/Entity Type
Real Estate
Look and feel
Each slider illustrates characteristics of the customer's brand and the style your logo design should communicate.

```html
<!DOCTYPE html>
<html lang="en">
<head>
<meta charset="utf-8">
<title>Oversized apartment in a lifestyle location</title>
<link href="https://fonts.googleapis.com/css2?family=Roboto:wght@300;400;700&display=swap" rel="stylesheet">
<style>
  :root{
    --ink:#1e1e1e;
    --panel:#3b3b3b;
    --white:#ffffff;
    --red:#d42a2b;
    --orange:#f39a12;
    --yellow:#fcc30e;
    --rule:#9a9a9a;
  }
  *{margin:0;padding:0;box-sizing:border-box}
  html,body{width:849px;height:1200px;overflow:hidden;background:var(--white)}
  body{font-family:"Roboto",Arial,sans-serif;color:var(--ink)}
  .flyer{position:relative;width:849px;height:1200px;overflow:hidden}
  .photo{position:absolute}
  .photo-hero{left:0;top:0;width:849px;height:502px;
    background:linear-gradient(180deg,#3b7fd6 0%,#8fb6e2 35%,#c2874f 60%,#b8a58c 100%)}
  .photo-pool{left:0;top:507px;width:421px;height:282px;
    background:linear-gradient(180deg,#2f7ad4 0%,#7aa3cf 30%,#b86a44 55%,#2fa9d8 80%,#9b8c78 100%)}
  .photo-kitchen{left:425px;top:507px;width:424px;height:282px;
    background:linear-gradient(160deg,#f1f0ec 0%,#dcdad4 55%,#c9c6bd 100%)}
  .brand{position:absolute;left:611px;top:32px;width:191px;height:62px;background:var(--white);
    display:flex;align-items:center;gap:10px;padding:0 14px}
  .brand-mark{width:22px;height:22px;background:var(--red);flex:none}
  .brand-name{font-size:25px;font-weight:700;color:var(--ink)}
  .headline{position:absolute;left:50px;top:806px;font-size:41px;font-weight:300;letter-spacing:-.2px;white-space:nowrap}
  .address{position:absolute;left:51px;top:872px;width:225px;white-space:nowrap}
  .address .street{font-size:20px;font-weight:300;line-height:24px}
  .address .suburb{font-size:23px;font-weight:700;line-height:28px;margin-top:3px}
  .divider-v{position:absolute;left:283px;top:866px;width:1px;height:116px;background:var(--rule)}
  .blurb{position:absolute;left:293px;top:868px;width:505px;font-size:12.6px;line-height:18.6px;font-weight:400}
  .details{position:absolute;left:0;top:994px;width:849px;height:206px;background:var(--panel);color:var(--white)}
  .stat{position:absolute;left:0;width:61px;text-align:center;color:var(--white)}
  .stat b{display:block;font-size:29px;font-weight:300;line-height:30px;padding-top:4px}
  .stat svg{display:block;margin:1px auto 0}
  .stat-bed{top:0;height:58px;background:var(--red)}
  .stat-bath{top:58px;height:58px;background:var(--orange)}
  .stat-car{top:116px;height:90px;background:var(--yellow)}
  .stat-car b{padding-top:12px}
  .features{position:absolute;left:106px;top:16px;width:380px;list-style:none;font-size:13.4px;font-weight:700;line-height:22px}
  .features li{position:relative;padding-left:11px}
  .features li::before{content:"";position:absolute;left:0;top:9px;width:4px;height:4px;border-radius:50%;background:var(--white)}
  .panel-rule{position:absolute;left:502px;top:12px;width:1px;height:182px;background:var(--rule)}
  .costs{position:absolute;left:522px;top:14px;font-size:13px;line-height:22.6px}
  .costs .row{display:flex}
  .costs .label{width:173px}
  .inspect{margin-top:10px}
  .contact small{font-size:10.3px}
  .contact.phone{padding-left:56px}
</style>
</head>
<body>
<div class="flyer">
  <div class="photo photo-hero" role="img" aria-label="Balcony terrace with curved railing looking over neighbouring apartments and sky"></div>
  <div class="brand"><span class="brand-mark"></span><span class="brand-name">Harbourline</span></div>
  <div class="photo photo-pool" role="img" aria-label="Outdoor swimming pool beside the brick apartment building"></div>
  <div class="photo photo-kitchen" role="img" aria-label="White kitchen with gas cooktop and wall oven"></div>

  <h1 class="headline">Oversized apartment in a lifestyle location</h1>
  <div class="address">
    <div class="street">19/17-25 Fern Street,</div>
    <div class="suburb">ELWYN JUNCTION</div>
  </div>
  <div class="divider-v"></div>
  <p class="blurb">Peacefully positioned on the 5th floor of a refurbished security building, this superbly spacious residence combines modern, low maintenance apartment living with inviting prospects for the entertainer. Boasting a huge full-width terrace on-title, its sought-after setting in the heart of Elwyn Junction offers the ultimate in lifestyle and convenience.</p>

  <section class="details">
    <div class="stat stat-bed"><b>2</b>
      <svg width="26" height="16" viewBox="0 0 26 16" fill="none" stroke="#fff" stroke-width="1.6"><path d="M2 2v13M2 11h22v4M2 8h22v3M5 8V5h7v3"/></svg>
    </div>
    <div class="stat stat-bath"><b>1</b>
      <svg width="26" height="18" viewBox="0 0 26 18" fill="none" stroke="#fff" stroke-width="1.6"><path d="M2 8h22M4 8v4a4 4 0 0 0 4 4h10a4 4 0 0 0 4-4V8M6 8V2h3M7 16l-1 2M19 16l1 2"/></svg>
    </div>
    <div class="stat stat-car"><b>1</b>
      <svg width="28" height="18" viewBox="0 0 28 18" fill="none" stroke="#fff" stroke-width="1.6"><path d="M3 12V8l4-6h14l4 6v4z"/><circle cx="8" cy="14" r="2.5"/><circle cx="20" cy="14" r="2.5"/></svg>
    </div>

    <ul class="features">
      <li>Expansive open plan living and dining area</li>
      <li>Terrace features city and Wattle Bay glimpses</li>
      <li>Kitchen updated with Vello gas appliances</li>
      <li>Built-ins in both bedrooms, fully tiled bathrooms</li>
      <li>Internal laundry, secure parking, lift, outdoor pool and gymnasium</li>
      <li>Steps to station, Eastgate Plaza and Ashgrove Park</li>
    </ul>

    <div class="panel-rule"></div>
    <div class="costs">
      <div class="row"><span class="label">Water Rates:</span><span>$ 0000 PQ</span></div>
      <div class="row"><span class="label">Council Rates:</span><span>$ 0000 PA</span></div>
      <div class="row"><span class="label">Strata Rates:</span><span>$ 0000 PA APPROX</span></div>
      <div class="row"><span class="label">Estimated Market Rental:</span><span>$700.00 p/w</span></div>
      <div class="inspect">Inspect : Sat 10:45 – 11:30; Wed 12:00 – 12:30</div>
      <div class="contact">Contact: Daniel Marsh <small>(Assisting owner in Private Sale)</small></div>
      <div class="contact phone">0400 123 456</div>
    </div>
  </section>
</div>
</body>
</html>
```